Book dust cover- front and back- 5.5x 8.5, white back ground, simple, testimonial on the back (just use sample words) price, qr code and picture of author. Front will include title and tagline
Tagline- Seven Mindsets to Stand Firm in Hard Seasons
Sorry, it didn't ask me specifically for everything.
Title: Walking Into Amber Light
Tagline: The 7 Mindsets to Overcome Life's Obstacles
Christian based- I use scripture and science to prove each mindset
No pink or girly looks
I like the covers like: Derek T Halloway's Books, Ironwilled, Fig and Kettle (words with little imagery- unless it really makes sense)
Females- 25-65
Christian

```html
<!DOCTYPE html>
<html lang="en">
<head>
<meta charset="utf-8">
<title>Walking Into Amber Light — Dust Cover Spread</title>
<link href="https://fonts.googleapis.com/css2?family=Cinzel:wght@400;500;600&family=Tinos:ital,wght@0,400;0,700&display=swap" rel="stylesheet">
<style>
  :root {
    --navy: #1a4f86;
    --paper: #ffffff;
    --edge: #dcdcdc;
    --ink: #2b2b2b;
    --muted: #9a9a9a;
    --silver-band: linear-gradient(90deg, #d4d4d4 0%, #6e6e6e 28%, #f0f0f0 52%, #555 78%, #cfcfcf 100%);
  }
  * { margin: 0; padding: 0; box-sizing: border-box; }
  html, body { width: 1200px; height: 1200px; overflow: hidden; background: var(--paper); }
  .canvas { position: relative; width: 1200px; height: 1200px; }
  .spread { position: absolute; left: 30px; top: 203px; width: 1140px; height: 793px; }
  .panel { position: absolute; top: 0; height: 793px; border: 1px solid var(--edge); background: var(--paper); overflow: hidden; }
  .back-cover { left: 0; width: 546px; }
  .spine { left: 545px; width: 52px; }
  .front-cover { left: 596px; width: 544px; }

  .band { position: absolute; left: 0; right: 0; }
  .band-silver { background: var(--silver-band); height: 6px; }
  .band-navy { background: var(--navy); height: 17px; }

  .title-block { position: absolute; display: block; }
  .title-block text { font-family: "Cinzel", serif; fill: var(--navy); }
  .title-rule { stroke: #8a8a8a; stroke-width: 2; }

  .author-mark { position: absolute; left: 0; top: 0; display: block; }
  .author-mark text { font-family: "Cinzel", serif; font-weight: 600; }

  .blurb { position: absolute; top: 242px; font-family: "Tinos", serif; font-size: 13.4px; line-height: 17.9px; color: var(--ink); text-align: justify; }
  .blurb p + p { margin-top: 17.9px; }
  .blurb-left { left: 58px; width: 200px; }
  .blurb-right { left: 287px; width: 199px; }
  .column-divider { position: absolute; left: 272px; top: 245px; width: 1px; height: 292px; background: #bbb; }

  .author-photo { position: absolute; left: 58px; top: 608px; width: 73px; height: 73px; border: 1px solid #999; background: #f6f6f6; }
  .author-bio { position: absolute; left: 148px; top: 607px; width: 338px; font-family: "Tinos", serif; font-size: 13.4px; line-height: 17.9px; color: var(--ink); text-align: justify; }
  .author-bio strong { font-weight: 700; }

  .label-box { position: absolute; top: 712px; width: 147px; height: 64px; border: 1px solid #999; display: flex; align-items: center; justify-content: center; font-family: "Tinos", serif; font-size: 14px; color: var(--muted); }
  .price-box { left: 57px; }
  .code-box { left: 339px; }

  .spine-type { position: absolute; left: 0; top: 0; }
  .spine-type text { font-family: "Cinzel", serif; fill: var(--navy); }

  .tagline { position: absolute; left: 0; width: 544px; text-align: center; font-family: "Cinzel", serif; font-weight: 600; color: var(--navy); line-height: 1; }
  .tagline-main { top: 616px; font-size: 29px; letter-spacing: 1px; }
  .tagline-sub { top: 647px; font-size: 22.5px; letter-spacing: 0.3px; }
  .credo { position: absolute; left: 0; width: 544px; top: 731px; text-align: center; font-family: "Cinzel", serif; font-size: 13.6px; line-height: 16px; color: #a8a8a8; letter-spacing: 0.4px; }
</style>
</head>
<body>
<div class="canvas">
  <div class="spread">

    <section class="panel back-cover">
      <svg class="title-block" style="left:0;top:0" width="546" height="180" viewBox="0 0 546 180">
        <text x="176" y="70" font-size="64" textLength="205" lengthAdjust="spacingAndGlyphs">WALKING</text>
        <line class="title-rule" x1="176" y1="77" x2="381" y2="77"/>
        <text x="176" y="112" font-size="37" textLength="205" lengthAdjust="spacingAndGlyphs">INTO AMBER</text>
        <line class="title-rule" x1="176" y1="118" x2="381" y2="118"/>
        <text x="178" y="170" font-size="64" textLength="201" lengthAdjust="spacing">LIGHT</text>
      </svg>

      <div class="band band-silver" style="top:197px"></div>
      <div class="band band-navy" style="top:203px"></div>

      <div class="blurb blurb-left">
        <p>Lorem ipsum dolor sit amet, con adipiscing elit, sed diam nonummy nibh euismod tincidunt ut laoreet dolore magna aliquam erat volutpat. Ut wisi enim ad minim veniam, quis nostrud exerci tation ullamcorper suscipit lobortis nisl ut aliquip ex ea commodo consequat.</p>
        <p>Duis autem vel eum iriure dolor in hendrerit in vulputate velit esse molestie consequat, vel illum dolore eu feugiat nulla facilisis at vero eros et accumsan et iusto odio dignissim qui blandit praesent luptatum zzril delenit augue duis dolore te feugait nulla facilisi.</p>
      </div>
      <div class="column-divider"></div>
      <div class="blurb blurb-right">
        <p>Lorem ipsum dolor sit amet, cons ectetuer adipiscing elit, sed diam nonummy nibh euismod tincidunt ut laoreet dolore magna aliquam erat volutpat. Ut wisi enim ad minim veniam, quis nostrud exerci tation ullamcorper suscipit lobortis nisl ut aliquip ex ea commodo consequat. Lorem ipsum dolor sit amet, consectetuer adipiscing elit, sed diam nonummy nibh euismod tincidunt ut laoreet dolore magna aliquam erat volutpat. Ut wisi enim ad minim veniam, quis nostrud exerci tation ullamcorper suscipit lobortis nisl ut aliquip ex ea commodo consequat. Duis autem vel eum iriure.</p>
      </div>

      <div class="band band-navy" style="top:572px"></div>
      <div class="band band-silver" style="top:589px"></div>

      <div class="author-photo" role="img" aria-label="Author portrait photo"></div>
      <p class="author-bio"><strong>Authors Name:</strong> Lorem ipsum dolor sit amet, consectetuer adipiscing elit, sed diam nonummy nibh euismod tincidunt ut laoreet dolore magna aliquam erat volutpat. Ut wisi enim ad minim veniam.</p>

      <div class="band band-silver" style="top:692px"></div>

      <div class="label-box price-box">price</div>
      <div class="label-box code-box">barcode/qr code</div>
    </section>

    <section class="panel spine">
      <svg class="spine-type" width="52" height="793" viewBox="0 0 52 793">
        <text transform="translate(37 241) rotate(-90)" font-size="31" textLength="196" lengthAdjust="spacingAndGlyphs">A<tspan font-size="25">UTHORS</tspan> N<tspan font-size="25">AME</tspan></text>
        <text transform="translate(37 699) rotate(-90)" font-size="31" textLength="413" lengthAdjust="spacing">WALKING INTO AMBER LIGHT</text>
      </svg>
    </section>

    <section class="panel front-cover">
      <svg class="author-mark" width="544" height="190" viewBox="0 0 544 190">
        <defs>
          <linearGradient id="silverInk" x1="0" y1="0" x2="0" y2="1">
            <stop offset="0" stop-color="#d8d8d8"/>
            <stop offset="0.45" stop-color="#7a7a7a"/>
            <stop offset="0.6" stop-color="#b5b5b5"/>
            <stop offset="1" stop-color="#5f5f5f"/>
          </linearGradient>
        </defs>
        <text x="146" y="92" font-size="72" fill="url(#silverInk)" textLength="252" lengthAdjust="spacingAndGlyphs">A<tspan font-size="56">UTHORS</tspan></text>
        <text x="196" y="166" font-size="72" fill="url(#silverInk)" textLength="153" lengthAdjust="spacingAndGlyphs">N<tspan font-size="56">AME</tspan></text>
      </svg>

      <div class="band band-silver" style="top:197px"></div>
      <div class="band band-navy" style="top:203px"></div>

      <svg class="title-block" style="left:0;top:240px" width="544" height="310" viewBox="0 240 544 310">
        <text x="90" y="343" font-size="117" textLength="384" lengthAdjust="spacingAndGlyphs">WALKING</text>
        <line class="title-rule" x1="90" y1="358" x2="474" y2="358"/>
        <text x="90" y="421" font-size="69" textLength="384" lengthAdjust="spacingAndGlyphs">INTO AMBER</text>
        <line class="title-rule" x1="90" y1="434" x2="474" y2="434"/>
        <text x="92" y="533" font-size="117" textLength="380" lengthAdjust="spacing">LIGHT</text>
      </svg>

      <div class="band band-navy" style="top:572px"></div>
      <div class="band band-silver" style="top:589px"></div>

      <div class="tagline tagline-main">Seven Mindsets</div>
      <div class="tagline tagline-sub">To Stand Firm in Hard Seasons</div>

      <div class="band band-silver" style="top:692px"></div>

      <p class="credo">EACH MINDSET IS ROOTED IN<br>FAITH, SCRIPTURE AND CAREFUL RESEARCH</p>
    </section>

  </div>
</div>
</body>
</html>
```